showcase project portfolio

create power point of project portfolio
from word file and website using similar design template

https://www.brelvon.co.uk/

Target Market(s)

corporte

```html
<!DOCTYPE html>
<html lang="en">
<head>
<meta charset="utf-8">
<title>Projects Managed – Brelvon Design Studio Ltd</title>
<link href="https://fonts.googleapis.com/css2?family=Questrial&family=Tenor+Sans&display=swap" rel="stylesheet">
<style>
:root{
  --navy:#1f3a52;
  --navy-dark:#162b3d;
  --tan:#d3a985;
  --tan-light:#e2c3a6;
  --page:#e6e6e6;
  --panel:#f1f1f1;
  --white:#ffffff;
  --ink:#2a3d4f;
  --muted:#6b7884;
  --rule:#1f3a52;
}
*{box-sizing:border-box;margin:0;padding:0}
html,body{width:1049px;height:1200px;overflow:hidden}
body{background:var(--page);font-family:"Questrial",sans-serif;color:var(--ink);position:relative}
.slide{position:absolute;width:359px;height:202px;overflow:hidden;background:var(--white)}
.col-a{left:152px}.col-b{left:537px}
.row-1{top:50px}.row-2{top:274px}.row-3{top:499px}.row-4{top:723px}.row-5{top:947px}
.abs{position:absolute}
.art{position:absolute;inset:0}

/* cover */
.cover-brand{position:absolute;left:17px;top:28px}
.brand-name{font-family:"Questrial",sans-serif;font-size:14px;letter-spacing:2px;color:var(--navy);display:flex;align-items:center;gap:4px}
.brand-name .dot{width:6px;height:6px;border-radius:50%;background:var(--tan)}
.brand-tag{font-size:3.2px;letter-spacing:.3px;color:var(--navy);margin-top:8px}
.cover-title{position:absolute;left:17px;font-family:"Tenor Sans",sans-serif;font-size:22px;line-height:22px;letter-spacing:.5px}
.cover-by{position:absolute;left:17px;font-size:8.5px;line-height:9px;color:var(--navy)}
.cover-date{position:absolute;left:17px;font-size:5px;color:var(--navy)}
.is-dark .brand-name,.is-dark .brand-tag,.is-dark .cover-by,.is-dark .cover-date{color:var(--white)}

/* headers */
.logo-sm{position:absolute;right:12px;top:10px;text-align:right}
.logo-sm .brand-name{font-size:9px;letter-spacing:1.3px;justify-content:flex-end}
.logo-sm .brand-name .dot{width:4px;height:4px}
.logo-sm .brand-tag{font-size:2px;margin-top:3px;color:var(--muted)}
.logo-sm.on-dark .brand-name,.logo-sm.on-dark .brand-tag{color:var(--white)}

.footer{position:absolute;left:0;right:0;bottom:0;height:12px;background:linear-gradient(90deg,var(--navy) 0%,var(--navy) 55%,var(--tan) 100%);display:flex;align-items:center;justify-content:space-between;padding:0 18px;font-size:4px;color:var(--white)}

/* tasks */
.task-panel{position:absolute;left:0;top:0;width:109px;height:190px;border-top-right-radius:16px;background:linear-gradient(160deg,#2d4860,#142636)}
.task-panel h2{position:absolute;left:0;right:0;top:88px;text-align:center;font-family:"Tenor Sans",sans-serif;font-weight:400;font-size:15px;color:var(--tan);letter-spacing:.5px}
.task-list{list-style:none;position:absolute;display:flex;flex-direction:column}
.task-list li{display:flex;align-items:center;gap:4px;font-size:4.3px;line-height:5px;color:var(--navy);border-bottom:.5px solid var(--rule);height:20px}
.task-list li:last-child{border-bottom:none}
.task-list li::before{content:"»";color:var(--tan);font-size:7px;line-height:5px;flex:none}
.tasks-b .task-list li{height:15.8px}

.tasks-hero{position:absolute;left:0;top:0;width:359px;height:76px;background:linear-gradient(180deg,#243f57 0%,#152838 100%)}
.tasks-hero h2{position:absolute;left:0;right:0;top:28px;text-align:center;font-family:"Tenor Sans",sans-serif;font-weight:400;font-size:13px;color:var(--white)}
.task-card{position:absolute;top:56px;height:124px;background:var(--white);border-radius:5px;box-shadow:0 1px 4px rgba(0,0,0,.12);padding:6px 10px}
.task-card .task-list{position:static}

/* projects */
.proj-head{position:absolute;left:0;right:0;top:0;height:40px;background:var(--white)}
.proj-head h2{position:absolute;left:18px;top:9px;font-family:"Tenor Sans",sans-serif;font-weight:400;font-size:12.5px;color:var(--tan);letter-spacing:.6px}
.proj-head p{position:absolute;left:18px;top:25px;font-size:5.6px;color:var(--navy)}
.proj-body{position:absolute;left:0;right:0;top:40px;bottom:12px;background:var(--panel)}
.info{position:absolute;left:18px;width:105px}
.info .icon{width:10px;height:10px;display:block;margin-bottom:2px}
.info h3{font-weight:400;font-size:5.6px;color:var(--navy)}
.info p{font-size:5.6px;line-height:8px;color:var(--muted)}
.ph{position:absolute}
.ph-brick{background:linear-gradient(160deg,#6e4a3b,#8a5744 45%,#4b3a32)}
.ph-green{background:linear-gradient(160deg,#3f5530,#5d6b48 50%,#7a6a58)}
.ph-stone{background:linear-gradient(160deg,#7b7466,#9a8f80 50%,#5f5a52)}
.ph-house{background:linear-gradient(180deg,#6d7b8a 0%,#8b5a45 55%,#4a4a4a)}
.dw{position:absolute;background:#ffffff;border:.5px solid #e2e2e2}
.dw-yellow{background:linear-gradient(180deg,#fbfbf2,#f4f1c8 50%,#fafafa)}
</style>
</head>
<body>

<!-- Cover: light -->
<section class="slide col-a row-1">
  <svg class="art" viewBox="0 0 359 202" aria-hidden="true">
    <defs>
      <linearGradient id="sky1" x1="0" y1="0" x2="0" y2="1"><stop offset="0" stop-color="#8fa9bf"/><stop offset=".6" stop-color="#b47a60"/><stop offset="1" stop-color="#4f5458"/></linearGradient>
    </defs>
    <path d="M268,0 Q210,120 90,202 L78,202 Q200,118 262,0Z" fill="var(--navy)"/>
    <path d="M274,0 Q214,122 96,202 L90,202 Q210,120 268,0Z" fill="var(--tan)"/>
  </svg>
  <svg class="art" viewBox="0 0 359 202" role="img" aria-label="Photo of a four-storey brick and render apartment building with cars parked in front">
    <path d="M274,0 L359,0 L359,202 L96,202 Q214,122 274,0Z" fill="url(#sky1)"/>
  </svg>
  <div class="cover-brand"><div class="brand-name"><span class="dot"></span>BRELVON</div><div class="brand-tag">ARCHITECTURE TODAY, READY FOR TOMORROW</div></div>
  <h1 class="cover-title" style="top:88px;color:var(--tan)">PROJECTS<br>MANAGED</h1>
  <p class="cover-by" style="top:132px">by Brelvon Design<br>Studio Ltd</p>
  <p class="cover-date" style="top:168px">June, 2024</p>
</section>

<!-- Cover: dark -->
<section class="slide col-b row-1 is-dark" style="background:var(--navy)">
  <svg class="art" viewBox="0 0 359 202" role="img" aria-label="Photo of a four-storey brick and render apartment building with cars parked in front">
    <defs>
      <linearGradient id="sky2" x1="0" y1="0" x2="0" y2="1"><stop offset="0" stop-color="#8fa9bf"/><stop offset=".6" stop-color="#b47a60"/><stop offset="1" stop-color="#4f5458"/></linearGradient>
    </defs>
    <polygon points="248,0 359,0 359,202 152,202" fill="url(#sky2)"/>
    <polygon points="276,126 358,202 196,202" fill="var(--tan)"/>
  </svg>
  <div class="cover-brand" style="top:16px"><div class="brand-name"><span class="dot"></span>BRELVON</div><div class="brand-tag">ARCHITECTURE TODAY, READY FOR TOMORROW</div></div>
  <h1 class="cover-title" style="top:74px;color:var(--tan)">PROJECTS<br>MANAGED</h1>
  <p class="cover-by" style="top:118px">by Brelvon Design<br>Studio Ltd</p>
  <p class="cover-date" style="top:154px">June, 2024</p>
</section>

<!-- Cover: light alt -->
<section class="slide col-a row-2">
  <svg class="art" viewBox="0 0 359 202" role="img" aria-label="Photo of a four-storey brick and render apartment building with a car parked in front">
    <defs>
      <linearGradient id="sky3" x1="0" y1="0" x2="0" y2="1"><stop offset="0" stop-color="#8fa9bf"/><stop offset=".6" stop-color="#b47a60"/><stop offset="1" stop-color="#4f5458"/></linearGradient>
    </defs>
    <polygon points="243,0 359,0 359,202 140,202" fill="url(#sky3)"/>
    <polygon points="298,0 359,0 359,150" fill="var(--tan)"/>
    <polygon points="257,66 358,202 172,202" fill="var(--tan)"/>
  </svg>
  <div class="cover-brand"><div class="brand-name"><span class="dot"></span>BRELVON</div><div class="brand-tag">ARCHITECTURE TODAY, READY FOR TOMORROW</div></div>
  <h1 class="cover-title" style="top:88px;color:var(--navy)">PROJECTS<br>MANAGED</h1>
  <p class="cover-by" style="top:132px">by Brelvon Design<br>Studio Ltd</p>
  <p class="cover-date" style="top:168px">June, 2024</p>
</section>

<!-- Tasks: side panel -->
<section class="slide col-b row-2 tasks-b">
  <div class="task-panel" role="img" aria-label="Dusk photo of a modern gabled house"><h2>TASKS</h2></div>
  <div class="logo-sm"><div class="brand-name"><span class="dot"></span>BRELVON</div><div class="brand-tag">ARCHITECTURE TODAY, READY FOR TOMORROW</div></div>
  <ul class="task-list" style="left:118px;top:30px;width:111px">
    <li>Creating working drawings</li>
    <li>Price breakdown of total build costs</li>
    <li>Liaising with Marlow Vale Water for water connection, drainage connection</li>
    <li>Liaising with Northfen Gas to get gas supply to site</li>
    <li>Liaising with Meridian Power Grid to get electric supply</li>
    <li>Tendering out works to different tradesman</li>
    <li>Getting material orders</li>
  </ul>
  <ul class="task-list" style="left:236px;top:30px;width:111px">
    <li>Arranging structural engineer for the site</li>
    <li>Arranging Building control for the site</li>
    <li>Making sure material is on site on time</li>
    <li>Making sure all tradesman work is up to current British standards</li>
    <li>Daily walk rounds to check work is done according to approved plans</li>
    <li>Placing orders for bathrooms, kitchen, and flooring</li>
    <li>All snag work with main contactor</li>
  </ul>
  <div class="footer"><span>Brelvon Design Studio Ltd</span><span>4</span></div>
</section>

<!-- Tasks: cards -->
<section class="slide col-a row-3">
  <div class="tasks-hero" role="img" aria-label="Dusk photo of modern gabled houses"><h2>TASKS</h2></div>
  <div class="logo-sm on-dark"><div class="brand-name"><span class="dot"></span>BRELVON</div><div class="brand-tag">ARCHITECTURE TODAY, READY FOR TOMORROW</div></div>
  <div class="task-card" style="left:18px;width:159px">
    <ul class="task-list">
      <li style="height:16px">Creating working drawings</li>
      <li style="height:16px">Price breakdown of total build costs</li>
      <li style="height:16px">Liaising with Marlow Vale Water for water connection, drainage connection</li>
      <li style="height:16px">Liaising with Northfen Gas to get gas supply to site</li>
      <li style="height:16px">Liaising with Meridian Power Grid to get electric supply</li>
      <li style="height:16px">Tendering out works to different tradesman</li>
      <li style="height:16px">Getting material orders</li>
    </ul>
  </div>
  <div class="task-card" style="left:182px;width:159px">
    <ul class="task-list">
      <li style="height:16px">Arranging structural engineer for the site</li>
      <li style="height:16px">Arranging Building control for the site</li>
      <li style="height:16px">Making sure material is on site on time</li>
      <li style="height:16px">Making sure all tradesman work is up to current British standards</li>
      <li style="height:16px">Daily walk rounds to check work is done according to approved plans</li>
      <li style="height:16px">Placing orders for bathrooms, kitchen, and flooring</li>
      <li style="height:16px">All snag work with main contactor</li>
    </ul>
  </div>
  <div class="footer"><span>Brelvon Design Studio Ltd</span><span>5</span></div>
</section>

<!-- Project one -->
<section class="slide col-b row-3">
  <header class="proj-head"><h2>PROJECT ONE</h2><p>Garages at Ashcombe Mews, Ashcombe Street, Derby</p>
    <div class="logo-sm"><div class="brand-name"><span class="dot"></span>BRELVON</div><div class="brand-tag">ARCHITECTURE TODAY, READY FOR TOMORROW</div></div></header>
  <div class="proj-body"></div>
  <div class="info" style="top:49px">
    <svg class="icon" viewBox="0 0 10 10" aria-hidden="true"><circle cx="5" cy="5" r="4.5" fill="none" stroke="var(--navy)" stroke-width=".6"/><rect x="3.2" y="2.6" width="3.6" height="4.6" fill="none" stroke="var(--navy)" stroke-width=".5"/><path d="M3.9 4h2.2M3.9 5h2.2M3.9 6h1.4" stroke="var(--navy)" stroke-width=".4"/></svg>
    <h3>Proposal:</h3>
    <p>Change of use from garages to two dwelling houses (use class C3) including alterations to the front and side elevations</p>
  </div>
  <div class="ph ph-green" style="left:129px;top:49px;width:88px;height:64px" role="img" aria-label="Photo of the existing brick garages along a lane"></div>
  <div class="ph ph-brick" style="left:129px;top:118px;width:88px;height:64px" role="img" aria-label="Photo of the garage row from the mews entrance"></div>
  <div class="dw dw-yellow" style="left:222px;top:49px;width:126px;height:133px" role="img" aria-label="Floor plans and elevations of the proposed dwellings"></div>
  <div class="footer"><span>Brelvon Design Studio Ltd</span><span>6</span></div>
</section>

<!-- Project two -->
<section class="slide col-a row-4">
  <header class="proj-head"><h2>PROJECT TWO</h2><p>Lorem Ipsum is simply dummy text of the printing and typesetting industry.</p>
    <div class="logo-sm"><div class="brand-name"><span class="dot"></span>BRELVON</div><div class="brand-tag">ARCHITECTURE TODAY, READY FOR TOMORROW</div></div></header>
  <div class="proj-body"></div>
  <div class="info" style="top:49px">
    <svg class="icon" viewBox="0 0 10 10" aria-hidden="true"><circle cx="5" cy="5" r="4.5" fill="none" stroke="var(--navy)" stroke-width=".6"/><path d="M5 7.6C3.6 6 3.2 5.2 3.2 4.3a1.8 1.8 0 0 1 3.6 0c0 .9-.4 1.7-1.8 3.3z" fill="none" stroke="var(--navy)" stroke-width=".5"/><circle cx="5" cy="4.3" r=".6" fill="var(--navy)"/></svg>
    <h3>Location:</h3>
    <p>48 Fellgate Road, Derby</p>
    <svg class="icon" style="margin-top:8px" viewBox="0 0 10 10" aria-hidden="true"><circle cx="5" cy="5" r="4.5" fill="none" stroke="var(--navy)" stroke-width=".6"/><rect x="3.2" y="2.6" width="3.6" height="4.6" fill="none" stroke="var(--navy)" stroke-width=".5"/><path d="M3.9 4h2.2M3.9 5h2.2M3.9 6h1.4" stroke="var(--navy)" stroke-width=".4"/></svg>
    <h3>Proposal:</h3>
    <p>Change of use from offices (use class B1) to 12 flats (use class C3)</p>
  </div>
  <div class="ph ph-brick" style="left:129px;top:49px;width:88px;height:64px" role="img" aria-label="Photo of the red brick office building"></div>
  <div class="ph ph-green" style="left:129px;top:118px;width:88px;height:64px" role="img" aria-label="Photo of the building's rear courtyard"></div>
  <div class="dw" style="left:223px;top:49px;width:126px;height:133px" role="img" aria-label="Floor plans for the twelve proposed flats"></div>
  <div class="footer"><span>Brelvon Design Studio Ltd</span><span>7</span></div>
</section>

<!-- Project three -->
<section class="slide col-b row-4">
  <header class="proj-head"><h2>PROJECT THREE</h2><p>Lorem Ipsum is simply dummy text of the printing and typesetting industry.</p>
    <div class="logo-sm"><div class="brand-name"><span class="dot"></span>BRELVON</div><div class="brand-tag">ARCHITECTURE TODAY, READY FOR TOMORROW</div></div></header>
  <div class="proj-body"></div>
  <div class="info" style="top:49px">
    <svg class="icon" viewBox="0 0 10 10" aria-hidden="true"><circle cx="5" cy="5" r="4.5" fill="none" stroke="var(--navy)" stroke-width=".6"/><path d="M5 7.6C3.6 6 3.2 5.2 3.2 4.3a1.8 1.8 0 0 1 3.6 0c0 .9-.4 1.7-1.8 3.3z" fill="none" stroke="var(--navy)" stroke-width=".5"/><circle cx="5" cy="4.3" r=".6" fill="var(--navy)"/></svg>
    <h3>Location:</h3>
    <p>12-16 Corran Street Derby</p>
    <svg class="icon" style="margin-top:8px" viewBox="0 0 10 10" aria-hidden="true"><circle cx="5" cy="5" r="4.5" fill="none" stroke="var(--navy)" stroke-width=".6"/><rect x="3.2" y="2.6" width="3.6" height="4.6" fill="none" stroke="var(--navy)" stroke-width=".5"/><path d="M3.9 4h2.2M3.9 5h2.2M3.9 6h1.4" stroke="var(--navy)" stroke-width=".4"/></svg>
    <h3>Proposal:</h3>
    <p style="line-height:8px">Refurbishment Of Commercial Ground Floor Units Together With Formation Of 6 Residential Units On First And Second Floors. Installation Of Glazing And Repair To External Masonry Including Bricking Up Of Existing Openings</p>
  </div>
  <div class="ph ph-stone" style="left:129px;top:49px;width:107px;height:64px" role="img" aria-label="Photo of the corner building on the street"></div>
  <div class="ph ph-brick" style="left:241px;top:49px;width:107px;height:64px" role="img" aria-label="Photo of the building's side elevation"></div>
  <div class="dw dw-yellow" style="left:129px;top:119px;width:219px;height:63px" role="img" aria-label="Floor plans of the six residential units"></div>
  <div class="footer"><span>Brelvon Design Studio Ltd</span><span>8</span></div>
</section>

<!-- Project four -->
<section class="slide col-a row-5">
  <header class="proj-head"><h2>PROJECT FOUR</h2><p>Lorem Ipsum is simply dummy text of the printing and typesetting industry.</p>
    <div class="logo-sm"><div class="brand-name"><span class="dot"></span>BRELVON</div><div class="brand-tag">ARCHITECTURE TODAY, READY FOR TOMORROW</div></div></header>
  <div class="proj-body"></div>
  <div class="info" style="top:49px">
    <svg class="icon" viewBox="0 0 10 10" aria-hidden="true"><circle cx="5" cy="5" r="4.5" fill="none" stroke="var(--navy)" stroke-width=".6"/><path d="M5 7.6C3.6 6 3.2 5.2 3.2 4.3a1.8 1.8 0 0 1 3.6 0c0 .9-.4 1.7-1.8 3.3z" fill="none" stroke="var(--navy)" stroke-width=".5"/><circle cx="5" cy="4.3" r=".6" fill="var(--navy)"/></svg>
    <h3>Location:</h3>
    <p>Land At 3 Holloway Park<br>Derby DE99 1ZZ</p>
    <svg class="icon" style="margin-top:6px" viewBox="0 0 10 10" aria-hidden="true"><circle cx="5" cy="5" r="4.5" fill="none" stroke="var(--navy)" stroke-width=".6"/><rect x="3.2" y="2.6" width="3.6" height="4.6" fill="none" stroke="var(--navy)" stroke-width=".5"/><path d="M3.9 4h2.2M3.9 5h2.2M3.9 6h1.4" stroke="var(--navy)" stroke-width=".4"/></svg>
    <h3>Proposal:</h3>
    <p>Erection of a dwelling house (use class C3)</p>
  </div>
  <div class="ph ph-green" style="left:129px;top:49px;width:107px;height:64px" role="img" aria-label="Photo of the overgrown plot"></div>
  <div class="ph ph-house" style="left:241px;top:49px;width:107px;height:64px" role="img" aria-label="Photo of the completed brick detached house"></div>
  <div class="dw dw-yellow" style="left:129px;top:118px;width:107px;height:64px" role="img" aria-label="Floor plans of the proposed house"></div>
  <div class="dw" style="left:241px;top:118px;width:107px;height:64px" role="img" aria-label="Proposed front elevation drawing"></div>
  <div class="footer"><span>Brelvon Design Studio Ltd</span><span>9</span></div>
</section>

<!-- Project five -->
<section class="slide col-b row-5">
  <header class="proj-head"><h2>PROJECT FIVE</h2><p>Lorem Ipsum is simply dummy text of the printing and typesetting industry.</p>
    <div class="logo-sm"><div class="brand-name"><span class="dot"></span>BRELVON</div><div class="brand-tag">ARCHITECTURE TODAY, READY FOR TOMORROW</div></div></header>
  <div class="proj-body"></div>
  <div class="info" style="top:49px">
    <svg class="icon" viewBox="0 0 10 10" aria-hidden="true"><circle cx="5" cy="5" r="4.5" fill="none" stroke="var(--navy)" stroke-width=".6"/><path d="M5 7.6C3.6 6 3.2 5.2 3.2 4.3a1.8 1.8 0 0 1 3.6 0c0 .9-.4 1.7-1.8 3.3z" fill="none" stroke="var(--navy)" stroke-width=".5"/><circle cx="5" cy="4.3" r=".6" fill="var(--navy)"/></svg>
    <h3>Location:</h3>
    <p>19, Wrenford Street, Birmingham</p>
    <svg class="icon" style="margin-top:14px" viewBox="0 0 10 10" aria-hidden="true"><circle cx="5" cy="5" r="4.5" fill="none" stroke="var(--navy)" stroke-width=".6"/><rect x="3.2" y="2.6" width="3.6" height="4.6" fill="none" stroke="var(--navy)" stroke-width=".5"/><path d="M3.9 4h2.2M3.9 5h2.2M3.9 6h1.4" stroke="var(--navy)" stroke-width=".4"/></svg>
    <h3>Proposal:</h3>
    <p>Warehouse conversion<br>to 4 town houses.</p>
  </div>
  <div class="ph ph-brick" style="left:129px;top:49px;width:107px;height:64px" role="img" aria-label="Photo of the brick warehouse facade"></div>
  <div class="ph ph-brick" style="left:241px;top:49px;width:107px;height:64px" role="img" aria-label="Photo of the warehouse's arched upper windows"></div>
  <div class="dw" style="left:129px;top:118px;width:107px;height:64px" role="img" aria-label="Floor plans of the four town houses"></div>
  <div class="ph ph-brick" style="left:241px;top:118px;width:107px;height:64px" role="img" aria-label="Photo of the warehouse courtyard"></div>
  <div class="footer"><span>Brelvon Design Studio Ltd</span><span>10</span></div>
</section>

</body>
</html>
```